Business Card Design

Business card design.

Business card is to have logo, website address and email address.

Website is www.brightkettle.ie
Email is info@brightkettle.ie
Logo uploaded

I have ordered Business Card Printing via Print Harbor, the Double-sided colour printed option with gloss finish.

Industry/Entity Type

Business

```html
<!DOCTYPE html>
<html lang="en">
<head>
<meta charset="utf-8">
<title>BrightKettle.ie Business Card</title>
<link rel="stylesheet" href="https://fonts.googleapis.com/css2?family=Poppins:wght@600;700&display=swap">
<style>
  :root {
    --paper: #ffffff;
    --ink: #050505;
    --steel-light: #6a6a6a;
    --steel-mid: #4a4a4a;
    --steel-dark: #2e2e2e;
    --accent: #d40000;
    --accent-dark: #8a0000;
  }
  html, body {
    margin: 0;
    padding: 0;
    width: 1040px;
    height: 1200px;
    overflow: hidden;
    background: var(--paper);
  }
  .canvas {
    position: relative;
    width: 1040px;
    height: 1200px;
  }
  .card {
    position: absolute;
    left: 36px;
    width: 970px;
    height: 554px;
    overflow: hidden;
    font-family: "Poppins", "Arial", sans-serif;
  }
  .card--front { top: 28px; }
  .card--back { top: 620px; }

  .steel-surface {
    position: absolute;
    inset: 0;
    background:
      radial-gradient(ellipse at 50% 40%, var(--steel-light) 0%, var(--steel-mid) 45%, var(--steel-dark) 100%);
  }

  /* Front */
  .brand-dot {
    position: absolute;
    left: 410px;
    top: 150px;
    width: 150px;
    height: 150px;
    border-radius: 50%;
    background: var(--accent);
  }
  .brand-name {
    position: absolute;
    left: 0;
    right: 0;
    top: 318px;
    margin: 0;
    text-align: center;
    font-weight: 700;
    font-size: 82px;
    line-height: 1;
    letter-spacing: -1px;
    color: var(--ink);
    text-transform: uppercase;
  }

  /* Back */
  .band-frame {
    position: absolute;
    left: 0;
    right: 0;
    top: 153px;
    height: 244px;
    background: var(--paper);
  }
  .band {
    position: absolute;
    left: 0;
    right: 0;
    background: var(--ink);
  }
  .band--web { top: 175px; height: 56px; }
  .band--middle { top: 238px; height: 78px; }
  .band--mail { top: 323px; height: 54px; }

  .name-column {
    position: absolute;
    left: 31px;
    top: 0;
    width: 84px;
    height: 554px;
    background: var(--paper);
    border-left: 4px solid var(--ink);
    border-right: 4px solid var(--ink);
    box-sizing: border-box;
    display: flex;
    justify-content: center;
    align-items: flex-start;
  }
  .name-column__text {
    writing-mode: vertical-rl;
    margin: 18px 0 0;
    font-weight: 700;
    font-size: 50px;
    line-height: 1;
    letter-spacing: -1px;
    color: var(--ink);
    text-transform: uppercase;
  }
  .accent-dot {
    position: absolute;
    left: 116px;
    top: 226px;
    width: 100px;
    height: 100px;
    border-radius: 50%;
    background: var(--accent);
    box-shadow: 0 0 0 4px var(--accent-dark);
  }
  .contact {
    position: absolute;
    left: 278px;
    margin: 0;
    font-weight: 600;
    font-size: 42px;
    line-height: 1;
    color: var(--paper);
    text-transform: uppercase;
  }
  .contact--web { top: 184px; }
  .contact--mail { top: 329px; }
</style>
</head>
<body>
<div class="canvas">
  <section class="card card--front" aria-label="Card front">
    <div class="steel-surface" role="img" aria-label="Brushed steel texture background"></div>
    <div class="brand-dot"></div>
    <h1 class="brand-name">BrightKettle.ie</h1>
  </section>

  <section class="card card--back" aria-label="Card back">
    <div class="steel-surface" role="img" aria-label="Brushed steel texture background"></div>
    <div class="band-frame"></div>
    <div class="band band--web"></div>
    <div class="band band--middle"></div>
    <div class="band band--mail"></div>
    <div class="name-column">
      <p class="name-column__text">BrightKettle.ie</p>
    </div>
    <div class="accent-dot"></div>
    <p class="contact contact--web">www.brightkettle.ie</p>
    <p class="contact contact--mail">info@brightkettle.ie</p>
  </section>
</div>
</body>
</html>
```